NEW YORK Plumbing/utility company 10 year anniversary business card

Looking For simple back and front business card would like to include a few things in description
We offer 24/7 emergency service
residential
commercial
industrial
municipal
services offered
Plumbing
hydro excavation
hydro jetting
Well pumps
Sewer pumps
water mains
sewer mains

```html
<!DOCTYPE html>
<html lang="en">
<head>
<meta charset="utf-8">
<title>Ridgeline Water &amp; Sewer – Business Card</title>
<link href="https://fonts.googleapis.com/css2?family=Montserrat:wght@400;500;600;700;800&family=Roboto+Condensed:ital,wght@0,700;1,700;1,800&display=swap" rel="stylesheet">
<style>
  :root {
    --page-bg: #ece7df;
    --brand-blue: #1d5fa6;
    --deep-blue: #175497;
    --brand-red: #e3262b;
    --white: #ffffff;
    --line-light: rgba(255,255,255,0.35);
  }
  * { margin: 0; padding: 0; box-sizing: border-box; }
  html, body { width: 900px; height: 1200px; overflow: hidden; }
  body {
    background: var(--page-bg);
    font-family: "Montserrat", sans-serif;
    position: relative;
  }
  .card {
    position: absolute;
    left: 82px;
    width: 738px;
    height: 434px;
    border-radius: 40px;
    overflow: hidden;
  }
  .card-front { top: 128px; background: var(--white); }
  .card-back {
    top: 630px;
    background: linear-gradient(160deg, #2067b0 0%, var(--deep-blue) 60%, #1a5a9f 100%);
  }

  /* brand name block */
  .brand-name {
    position: absolute;
    width: 290px;
    font-weight: 800;
    line-height: 1;
    letter-spacing: 1px;
    white-space: nowrap;
    text-align: center;
  }
  .brand-name .primary { display: block; font-size: 48px; }
  .brand-name .secondary { display: block; font-size: 22px; margin-top: 14px; letter-spacing: 2.5px; }
  .card-front .brand-name { left: 40px; top: 60px; color: var(--brand-blue); }
  .card-back .brand-name { left: 80px; top: 175px; color: var(--white); }

  /* contact person */
  .person { position: absolute; right: 46px; top: 56px; text-align: right; }
  .person-name { font-size: 31px; color: var(--brand-blue); font-weight: 400; letter-spacing: 0.5px; }
  .person-name strong { font-weight: 700; }
  .person-title { font-size: 21px; color: var(--brand-red); font-weight: 500; margin-top: 4px; }

  /* contact lines */
  .contact { position: absolute; left: 42px; display: flex; align-items: center; gap: 14px; }
  .contact-phone { top: 278px; }
  .contact-email { top: 316px; }
  .contact-icon {
    width: 24px; height: 24px; background: var(--brand-red);
    display: flex; align-items: center; justify-content: center; border-radius: 3px;
  }
  .contact-phone .contact-text { font-size: 30px; font-weight: 700; color: var(--brand-blue); }
  .contact-email .contact-text { font-size: 18px; font-weight: 500; color: var(--brand-blue); }

  /* emergency badge */
  .emergency { position: absolute; left: 472px; top: 222px; width: 220px; height: 120px;
    font-family: "Roboto Condensed", sans-serif; font-style: italic; font-weight: 800; }
  .emergency span { position: absolute; line-height: 1; white-space: nowrap; }
  .emergency .two { left: 2px; top: 22px; font-size: 96px; color: var(--brand-blue); }
  .emergency .four { left: 42px; top: 22px; font-size: 96px; color: var(--brand-red); }
  .emergency .x7 { left: 98px; top: 2px; font-size: 46px; color: var(--brand-blue); }
  .emergency .we-offer { left: 0; top: 102px; font-size: 13px; color: var(--brand-blue); font-weight: 700; }
  .emergency .label-emergency { left: 98px; top: 56px; font-size: 25px; color: var(--brand-blue); font-weight: 700; }
  .emergency .label-service { left: 98px; top: 80px; font-size: 36px; color: var(--brand-red); }

  /* sector band */
  .sector-band { position: absolute; left: 0; top: 0; width: 738px; height: 434px; }
  .sectors {
    position: absolute; left: 40px; right: 46px; top: 400px;
    display: flex; justify-content: space-between; list-style: none;
  }
  .sectors li, .services li {
    display: flex; align-items: center; gap: 8px; color: var(--white); white-space: nowrap;
  }
  .sectors li { font-size: 19px; font-weight: 700; letter-spacing: 0.8px; }
  .drop {
    width: 10px; height: 10px; background: var(--white);
    border-radius: 50% 0 50% 50%; transform: rotate(-45deg); flex-shrink: 0;
  }

  /* back side */
  .back-wave { position: absolute; left: 0; top: 0; width: 738px; height: 434px; }
  .divider { position: absolute; left: 402px; top: 98px; width: 1px; height: 240px; background: var(--line-light); }
  .services { position: absolute; left: 436px; top: 94px; width: 212px; }
  .services h2 { font-size: 20px; font-weight: 700; color: var(--white); letter-spacing: 0; margin-bottom: 10px; white-space: nowrap; }
  .services ul { list-style: none; }
  .services li {
    font-size: 16px; font-weight: 500; letter-spacing: 0.3px;
    height: 31.6px; border-bottom: 1px solid var(--line-light);
  }
  .services li:last-child { border-bottom: none; }
</style>
</head>
<body>

<section class="card card-front">
  <div class="brand-name">
    <span class="primary">RIDGELINE</span>
    <span class="secondary">WATER &amp; SEWER</span>
  </div>

  <div class="person">
    <p class="person-name"><strong>DANIEL</strong> HARPER</p>
    <p class="person-title">CEO/FOUNDER</p>
  </div>

  <div class="contact contact-phone">
    <span class="contact-icon">
      <svg width="16" height="16" viewBox="0 0 24 24"><path fill="#fff" d="M6.6 10.8a15 15 0 0 0 6.6 6.6l2.2-2.2c.3-.3.7-.4 1-.2 1.1.4 2.3.6 3.6.6.6 0 1 .4 1 1V20c0 .6-.4 1-1 1A17 17 0 0 1 3 4c0-.6.4-1 1-1h3.5c.6 0 1 .4 1 1 0 1.3.2 2.5.6 3.6.1.3 0 .7-.2 1z"/></svg>
    </span>
    <span class="contact-text">845-555-0182</span>
  </div>
  <div class="contact contact-email">
    <span class="contact-icon">
      <svg width="16" height="12" viewBox="0 0 16 12"><rect x="0.75" y="0.75" width="14.5" height="10.5" fill="none" stroke="#fff" stroke-width="1.5"/><path d="M1 1l7 6 7-6" fill="none" stroke="#fff" stroke-width="1.5"/></svg>
    </span>
    <span class="contact-text">info@ridgelinews.com</span>
  </div>

  <div class="emergency" aria-label="We offer 24x7 emergency service">
    <span class="two">2</span>
    <span class="four">4</span>
    <span class="x7">X7</span>
    <span class="we-offer">WE OFFER</span>
    <span class="label-emergency">EMERGENCY</span>
    <span class="label-service">SERVICE</span>
  </div>

  <svg class="sector-band" viewBox="0 0 738 434" aria-hidden="true">
    <path d="M0,356 C220,372 480,378 738,366 L738,372 C480,386 220,386 0,384 Z" fill="var(--brand-red)"/>
    <path d="M0,380 C220,384 480,378 738,370 L738,434 L0,434 Z" fill="var(--brand-blue)"/>
  </svg>
  <ul class="sectors">
    <li><span class="drop"></span>RESIDENTIAL</li>
    <li><span class="drop"></span>COMMERCIAL</li>
    <li><span class="drop"></span>INDUSTRIAL</li>
    <li><span class="drop"></span>MUNICIPAL</li>
  </ul>
</section>

<section class="card card-back">
  <svg class="back-wave" viewBox="0 0 738 434" aria-hidden="true">
    <path d="M0,120 C200,40 420,60 738,150 L738,0 L0,0 Z" fill="rgba(255,255,255,0.04)"/>
    <path d="M300,434 C420,300 580,200 738,190 L738,434 Z" fill="rgba(255,255,255,0.05)"/>
  </svg>

  <div class="brand-name">
    <span class="primary">RIDGELINE</span>
    <span class="secondary">WATER &amp; SEWER</span>
  </div>

  <div class="divider"></div>

  <div class="services">
    <h2>SERVICES OFFERED</h2>
    <ul>
      <li><span class="drop"></span>PLUMBING</li>
      <li><span class="drop"></span>HYDRO EXCAVATION</li>
      <li><span class="drop"></span>HYDRO JETTING</li>
      <li><span class="drop"></span>WELL PUMPS</li>
      <li><span class="drop"></span>SEWER PUMPS</li>
      <li><span class="drop"></span>WATER MAINS</li>
      <li><span class="drop"></span>SEWER MAINS</li>
    </ul>
  </div>
</section>

</body>
</html>
```